I'm looking for a book cover with the Main title:
Where the Lanterns Drift Beyond the Harbour Mist at Dusk

Subtitle: A Wanderer's Chronicle of Salt and Ember

Looking for a clean design that attracts people to the book.

Open to all styles of design (plain text, animated characters, scenery) as long as the text is in basic font and easy to read.

This is to be put somewhere under the titles
Written By: Bogumil Trenkaro

The back of the book will have:

"A physical, mental, emotional, and spiritual guide to fat loss. Going beyond calorie deficit diets and working out for hours a day in order to achieve results. It will help you get to the root cause of weight gain and give you the tools you need to take charge of your health and your life.

You will learn:
- The Best Foods to Eat for Fat Loss
- The Foods You Need to Avoid
- How to Heal Your Hormones
- Strategies to Overcome Emotional Eating
- Mindset and Motivation Tactics
- How to Meditate Without Losing Your Mind

I created this book to help those struggling with losing fat in a healthy, holistic, and sustainable way. It’s my sincere hope that this book gives you what you need in order to achieve your goals. "

Please place the photo somewhere on the back as well if it fits with the design.

Thank you for your time!

```html
<!DOCTYPE html>
<html lang="en">
<head>
<meta charset="utf-8">
<title>Where the Lanterns Drift Beyond the Harbour Mist at Dusk — Cover Spread</title>
<link rel="stylesheet" href="https://fonts.googleapis.com/css2?family=Amatic+SC:wght@700&family=Merriweather:ital,wght@0,300;0,700;1,300&family=Source+Sans+3:wght@400;700&family=Tinos&display=swap">
<style>
  :root {
    --paper: #ffffff;
    --ink: #111111;
    --edge: #8a8a8a;
    --rose: #f05b7b;
    --mauve: #b574a0;
    --periwinkle: #6e7fc2;
    --photo-tone: #6d7f5a;
  }
  * { margin: 0; padding: 0; box-sizing: border-box; }
  html, body { width: 1200px; height: 823px; overflow: hidden; background: var(--paper); }
  .spread { position: relative; width: 1200px; height: 823px; }

  .panel { position: absolute; top: 16px; width: 558px; height: 792px; border: 1px solid var(--edge); }
  .back-cover { left: 19px; background: var(--paper); }
  .front-cover { left: 623px; background: linear-gradient(155deg, var(--rose) 0%, var(--mauve) 50%, var(--periwinkle) 100%); }

  .back-motif {
    position: absolute; left: 440px; top: 61px; width: 22px; height: 721px; border-radius: 11px;
    background: linear-gradient(180deg, var(--rose) 0%, var(--mauve) 50%, var(--periwinkle) 100%);
  }
  .front-motif {
    position: absolute; left: 712px; top: 170px; width: 380px; height: 470px; border-radius: 24px;
    background: linear-gradient(180deg, rgba(255,255,255,0.10) 0%, rgba(255,255,255,0.16) 100%);
  }

  .title-art { position: absolute; left: 0; top: 0; width: 1200px; height: 823px; }
  .cover-title { font-family: "Amatic SC", "Arial Narrow", sans-serif; font-weight: 700; fill: #fff; }

  .blurb {
    position: absolute; left: 41px; top: 61px; width: 362px;
    font-family: "Source Sans 3", "Myriad Pro", sans-serif; font-size: 15.4px; line-height: 26.5px; color: var(--ink);
  }
  .learn-heading {
    position: absolute; left: 41px; top: 249px;
    font-family: "Source Sans 3", sans-serif; font-weight: 700; font-size: 18.5px; color: var(--ink);
  }
  .learn-list {
    position: absolute; left: 41px; top: 277px; width: 390px; list-style: none;
    font-family: "Source Sans 3", sans-serif; font-weight: 700; font-size: 18.8px; line-height: 22px; color: var(--ink);
  }
  .learn-list li { position: relative; padding-left: 23px; margin-bottom: 10px; }
  .learn-list li::before {
    content: ""; position: absolute; left: 4px; top: 8px; width: 7px; height: 7px; border-radius: 50%; background: var(--ink);
  }
  .author-heading {
    position: absolute; left: 41px; top: 555px;
    font-family: "Merriweather", Georgia, serif; font-weight: 700; font-size: 18.8px; color: var(--ink); letter-spacing: 0.3px;
  }
  .author-photo {
    position: absolute; left: 44px; top: 583px; width: 108px; height: 108px; border-radius: 50%;
    background: radial-gradient(circle at 50% 40%, #a58a74 0%, #7e7a5c 45%, var(--photo-tone) 100%);
  }
  .author-note {
    position: absolute; left: 41px; top: 590px; width: 370px;
    font-family: "Merriweather", Georgia, serif; font-style: italic; font-weight: 300; font-size: 15.8px; line-height: 22.4px; color: var(--ink);
  }
  .author-note span { display: block; white-space: nowrap; }

  .front-subtitle {
    position: absolute; left: 623px; top: 55px; width: 558px; text-align: center;
    font-family: "Merriweather", Georgia, serif; font-weight: 300; font-size: 22.3px; letter-spacing: 0.6px; color: #fff;
  }
  .front-author {
    position: absolute; left: 623px; top: 713px; width: 558px; text-align: center;
    font-family: "Tinos", "Times New Roman", serif; font-size: 52px; color: #fff;
  }
</style>
</head>
<body>
<div class="spread">
  <section class="panel back-cover"></section>
  <section class="panel front-cover"></section>

  <div class="back-motif" role="img" aria-label="Decorative flowing line artwork"></div>
  <div class="front-motif" role="img" aria-label="Decorative outline artwork framing the title"></div>

  <svg class="title-art" viewBox="0 0 2324 1596" preserveAspectRatio="none" role="img" aria-label="Where the Lanterns Drift Beyond the Harbour Mist at Dusk">
    <g class="cover-title">
      <text x="1630" y="362" font-size="100" textLength="240" lengthAdjust="spacingAndGlyphs">WHERE THE</text>
      <text x="1572" y="585" font-size="270" textLength="360" lengthAdjust="spacingAndGlyphs">LANTERNS</text>
      <text x="1570" y="717" font-size="150" textLength="350" lengthAdjust="spacingAndGlyphs">DRIFT</text>
      <text x="1562" y="812" font-size="100" textLength="365" lengthAdjust="spacingAndGlyphs">BEYOND THE</text>
      <text x="1505" y="955" font-size="170" textLength="475" lengthAdjust="spacingAndGlyphs">HARBOUR</text>
      <text x="1452" y="1100" font-size="170" textLength="330" lengthAdjust="spacingAndGlyphs">MIST</text>
      <text x="1800" y="1100" font-size="80" textLength="60" lengthAdjust="spacingAndGlyphs">AT</text>
      <text x="1530" y="1228" font-size="160" textLength="400" lengthAdjust="spacingAndGlyphs">DUSK</text>
    </g>
  </svg>

  <p class="blurb">A physical, mental, emotional, and spiritual guide to fat loss. Going beyond calorie deficit diets and working out for hours a day in order to achieve results. It will help you get to the root cause of weight gain and give you the tools you need to take charge of your health and your life.</p>

  <h3 class="learn-heading">You will learn:</h3>
  <ul class="learn-list">
    <li>The Best Foods to Eat for Fat Loss</li>
    <li>The Foods You Need to Avoid</li>
    <li>How to Heal Your Hormones</li>
    <li>Strategies to Overcome Emotional Eating</li>
    <li>Mindset and Motivation Tactics</li>
    <li>How to Meditate Without Losing<br>Your Mind</li>
  </ul>

  <h3 class="author-heading">About the Author</h3>
  <div class="author-photo" role="img" aria-label="Portrait photo of the author, Bogumil Trenkaro"></div>
  <p class="author-note">
    <span style="padding-left:128px">I created this book to help</span>
    <span style="padding-left:140px">those struggling with losing</span>
    <span style="padding-left:141px">fat in a healthy, holistic, and</span>
    <span style="padding-left:141px">sustainable way. It’s my</span>
    <span style="padding-left:132px">sincere hope that this book</span>
    <span style="padding-left:108px">gives you what you need in order</span>
    <span>to achieve your goals.</span>
  </p>

  <p class="front-subtitle">A Wanderer's Chronicle of Salt and Ember</p>
  <p class="front-author">Bogumil Trenkaro</p>
</div>
</body>
</html>
```